PawHush business card

Looking for a fun and cool biz card for a new company with patent pending products. I have products to help and protect dogs hearing. My colors are pantone blue and orange.
Updates

Please add tag line: Protect the ones you love...even your PawHushes!

Target Market(s)

Animal/Dog lovers!

Industry/Entity Type

Retail

Contact Information for Business Card

I'm looking for something simple yet fun with all the info included for biz cards

Colors
0555a3
f78f20

Requirements
Must have
• Logo
Nice to have
• name, website and email
Should not have
• phone number

```html
<!DOCTYPE html>
<html lang="en">
<head>
<meta charset="utf-8">
<title>PawHush Business Card</title>
<link rel="stylesheet" href="https://fonts.googleapis.com/css2?family=Open+Sans:wght@400;700&family=Syncopate:wght@700&family=Tinos&display=swap">
<style>
  :root {
    --brand-blue: #0a2d86;
    --brand-orange: #fc5200;
    --ink-light: #ffffff;
    --backdrop: #dcdcdc;
    --shadow: rgba(0, 0, 0, 0.22);
  }
  * { box-sizing: border-box; }
  html, body {
    margin: 0;
    width: 1200px;
    height: 944px;
    overflow: hidden;
    background: var(--backdrop);
  }
  .canvas {
    position: relative;
    width: 1200px;
    height: 944px;
  }
  .card {
    position: absolute;
    width: 560px;
    height: 320px;
    box-shadow: 0 14px 28px var(--shadow);
    overflow: hidden;
  }
  .card-band { position: absolute; left: 0; top: 0; }
  .card-back { left: 60px; top: 110px; background: var(--brand-blue); }
  .card-front { left: 580px; top: 510px; background: var(--brand-orange); }

  .wordmark {
    position: absolute;
    font-family: "Open Sans", sans-serif;
    font-weight: 700;
    letter-spacing: -1px;
    line-height: 1;
  }
  .card-back .wordmark {
    left: 0; right: 0; top: 76px;
    text-align: center;
    font-size: 84px;
    color: var(--brand-orange);
  }
  .tagline {
    position: absolute;
    left: 0; right: 0; top: 176px;
    margin: 0;
    text-align: center;
    font-family: "Open Sans", sans-serif;
    font-size: 14px;
    color: var(--ink-light);
  }
  .card-front .wordmark {
    left: 40px; top: 128px;
    font-size: 44px;
    color: var(--brand-blue);
  }
  .website {
    position: absolute;
    font-family: "Tinos", serif;
    font-size: 19px;
    color: var(--ink-light);
    display: flex;
    align-items: center;
    gap: 8px;
  }
  .card-back .website { left: 212px; top: 226px; }
  .card-front .website { left: 236px; top: 238px; }

  .holder {
    position: absolute;
    left: 300px; top: 40px;
    color: var(--ink-light);
  }
  .holder-name {
    font-family: "Syncopate", sans-serif;
    font-weight: 700;
    font-size: 20px;
    letter-spacing: 1px;
    padding-bottom: 6px;
    border-bottom: 1px solid var(--ink-light);
    margin: 0;
  }
  .holder-role {
    font-family: "Open Sans", sans-serif;
    font-size: 12px;
    margin: 6px 0 0 16px;
  }
  .contact-list {
    position: absolute;
    left: 320px; top: 112px;
    margin: 0; padding: 0;
    list-style: none;
    font-family: "Tinos", serif;
    font-size: 15px;
    color: var(--ink-light);
    line-height: 1.2;
  }
  .contact-list li {
    display: flex;
    align-items: center;
    gap: 9px;
    margin-bottom: 12px;
  }
  .icon { width: 20px; height: 20px; flex: none; display: block; }
</style>
</head>
<body>
<main class="canvas">

  <section class="card card-back" aria-label="Card back side">
    <svg class="card-band" width="560" height="320" viewBox="0 0 560 320" aria-hidden="true">
      <path fill="var(--brand-orange)" d="M0,236 H168 Q180,236 184,248 Q188,262 202,262 H392 Q404,262 406,250 V214 Q406,196 424,196 H560 V320 H0 Z"/>
    </svg>
    <div class="wordmark">PawHush</div>
    <p class="tagline">Protect the ones you love...even your PawHushes!</p>
    <div class="website">www.pawhush.com</div>
  </section>

  <section class="card card-front" aria-label="Card front side">
    <svg class="card-band" width="560" height="320" viewBox="0 0 560 320" aria-hidden="true">
      <path fill="var(--brand-blue)" d="M0,248 H206 Q218,248 222,260 Q226,276 240,276 H432 Q444,276 446,262 V214 Q446,196 464,196 H560 V320 H0 Z"/>
    </svg>

    <div class="wordmark">PawHush</div>

    <div class="holder">
      <p class="holder-name">DANA REYES</p>
      <p class="holder-role">Designation</p>
    </div>

    <ul class="contact-list">
      <li>
        <svg class="icon" viewBox="0 0 20 20" aria-hidden="true"><circle cx="10" cy="10" r="9" fill="none" stroke="#fff" stroke-width="1.5"/><path d="M10 15 C7 11.5 6.5 10 6.5 8.5 a3.5 3.5 0 0 1 7 0 c0 1.5 -0.5 3 -3.5 6.5z" fill="#fff"/><circle cx="10" cy="8.5" r="1.3" fill="var(--brand-orange)"/></svg>
        <span>Rue des Lilas 41<br>CH-1204 Genève</span>
      </li>
      <li>
        <svg class="icon" viewBox="0 0 20 20" aria-hidden="true"><circle cx="10" cy="10" r="9" fill="none" stroke="#fff" stroke-width="1.5"/><rect x="5.5" y="7" width="9" height="6.5" fill="#fff"/><path d="M5.5 7 L10 10.8 L14.5 7" fill="none" stroke="var(--brand-orange)" stroke-width="1"/></svg>
        <span>info@pawhush.com</span>
      </li>
    </ul>

    <div class="website">
      <svg class="icon" viewBox="0 0 20 20" aria-hidden="true"><circle cx="10" cy="10" r="9" fill="none" stroke="#fff" stroke-width="1.5"/><circle cx="10" cy="10" r="5" fill="none" stroke="#fff" stroke-width="1"/><ellipse cx="10" cy="10" rx="2" ry="5" fill="none" stroke="#fff" stroke-width="1"/><line x1="5" y1="10" x2="15" y2="10" stroke="#fff" stroke-width="1"/></svg>
      <span>www.pawhush.com</span>
    </div>
  </section>

</main>
</body>
</html>
```